Re-design of Business Card

We require a design for our business card.

Korrim is a supplier of industrial packaging specializing in plastic products. We are undergoing a rebranding to appear more corporate. We have changed our company name to korrim and have a new logo.

I have uploaded our old card design with the previous company name.
Don't copy the current design. We are looking for a new design.

Industry/Entity Type

Manufacturing

Contact Information for Business Card

please don't copy the current design. we are looking for a new design.

Font styles to use
Sans Serif

Colors

Designer to choose colors to be used in the design.

Requirements
Must have
• clean and easy to read.

```html
<!DOCTYPE html>
<html lang="en">
<head>
<meta charset="utf-8">
<title>Korrim Business Card</title>
<link rel="stylesheet" href="https://fonts.googleapis.com/css2?family=Lato:wght@400;700;900&display=swap">
<style>
  :root {
    --brand-orange: #f38024;
    --card-white: #ffffff;
    --ink: #1e1e1e;
    --backdrop: #2b2b2b;
  }
  * { box-sizing: border-box; margin: 0; padding: 0; }
  html, body {
    width: 1200px;
    height: 878px;
    overflow: hidden;
    background: var(--backdrop);
    font-family: "Lato", sans-serif;
  }
  .canvas {
    position: relative;
    width: 1200px;
    height: 878px;
  }
  .card {
    position: absolute;
    left: 290px;
    width: 620px;
    height: 354px;
  }
  .card-front {
    top: 65px;
    background: var(--brand-orange);
    display: flex;
    align-items: center;
    justify-content: center;
  }
  .front-wordmark {
    color: var(--card-white);
    font-weight: 900;
    font-size: 92px;
    letter-spacing: 2px;
  }
  .card-back {
    top: 459px;
    background: var(--card-white);
    display: flex;
    align-items: center;
  }
  .back-wordmark {
    width: 300px;
    text-align: center;
    color: var(--brand-orange);
    font-weight: 900;
    font-size: 62px;
    letter-spacing: 1px;
  }
  .divider {
    width: 2px;
    height: 170px;
    background: var(--brand-orange);
  }
  .details {
    padding-left: 30px;
    color: var(--ink);
  }
  .person-name {
    color: var(--brand-orange);
    font-weight: 700;
    font-size: 27px;
    line-height: 1.1;
  }
  .person-title {
    font-size: 15px;
    margin-bottom: 12px;
  }
  .address {
    font-size: 15px;
    line-height: 1.3;
    margin-bottom: 8px;
  }
  .contact-line {
    display: flex;
    align-items: center;
    gap: 10px;
    font-size: 15px;
    line-height: 1.45;
  }
  .contact-line svg {
    width: 14px;
    height: 14px;
    flex: none;
  }
</style>
</head>
<body>
<div class="canvas">
  <section class="card card-front">
    <div class="front-wordmark">KORRIM</div>
  </section>

  <section class="card card-back">
    <div class="back-wordmark">KORRIM</div>
    <div class="divider"></div>
    <div class="details">
      <h1 class="person-name">Dana Merrow</h1>
      <p class="person-title">Machinery Sales Manager</p>
      <p class="address">48 Tallow St Brookfield Park,<br>Qld 4072 Australia</p>
      <p class="contact-line">
        <svg viewBox="0 0 24 24" aria-hidden="true"><path fill="#f38024" d="M6.6 10.8c1.4 2.8 3.8 5.1 6.6 6.6l2.2-2.2c.3-.3.7-.4 1-.2 1.1.4 2.3.6 3.6.6.6 0 1 .4 1 1V20c0 .6-.4 1-1 1C10.6 21 3 13.4 3 4c0-.6.4-1 1-1h3.5c.6 0 1 .4 1 1 0 1.3.2 2.5.6 3.6.1.3 0 .7-.2 1z"/></svg>
        1300 415 806
      </p>
      <p class="contact-line">
        <svg viewBox="0 0 24 24" aria-hidden="true"><rect x="2" y="5" width="20" height="14" fill="#f38024"/><path d="M2 5l10 8 10-8" fill="none" stroke="#fff" stroke-width="1.6"/></svg>
        dana@korrim.com.au
      </p>
      <p class="contact-line">
        <svg viewBox="0 0 24 24" aria-hidden="true"><g fill="none" stroke="#f38024" stroke-width="2"><circle cx="12" cy="12" r="9"/><ellipse cx="12" cy="12" rx="4" ry="9"/><path d="M3 12h18M5 7h14M5 17h14"/></g></svg>
        www.korrim.com.au
      </p>
    </div>
  </section>
</div>
</body>
</html>
```